OpenCart website

We have an existing site that was based on open cart in 2011 but customised heavily. We want a brand new open cart site designed from scratch so we can work on transitioning the existing opencart database over after the project is done

Current site: www.quillfernstores.com

```html
<!DOCTYPE html>
<html lang="en">
<head>
<meta charset="utf-8">
<title>Quillfern Housewares</title>
<link href="https://fonts.googleapis.com/css2?family=Roboto:wght@400;500;700&display=swap" rel="stylesheet">
<style>
:root{
  --red:#e0141e;
  --ink:#1c1c1c;
  --muted:#6f6f6f;
  --line:#dcdcdc;
  --card:#efefef;
  --star:#f2b01e;
  --star-off:#c9c9c9;
  --white:#ffffff;
}
*{box-sizing:border-box;margin:0;padding:0}
html,body{width:1200px;height:3696px;overflow:hidden;background:var(--white)}
body{position:relative;font-family:'Roboto',Arial,sans-serif;color:var(--ink)}
.abs{position:absolute}
a{color:inherit;text-decoration:none}

/* header */
.topbar-links{left:160px;top:32px;font-size:13px}
.brand{left:500px;width:200px;text-align:center;color:var(--red);font-weight:700;font-size:22px;line-height:24px;letter-spacing:1px;text-transform:uppercase}
.brand-top{top:12px}
.header-icons{left:866px;top:20px;display:flex;gap:20px}
.cart-box{left:968px;top:0;width:57px;height:66px;background:var(--red);display:flex;align-items:center;justify-content:center}
.cart-count{position:absolute;top:6px;right:9px;color:var(--white);font-size:10px}
.header-rule{left:0;top:115px;width:1200px;height:1px;background:var(--line)}
.main-nav{top:141px;left:0;width:1200px;display:flex;justify-content:center;gap:24px;font-size:16px;font-weight:500}

/* hero */
.hero{left:162px;top:187px;width:876px;height:473px;background:linear-gradient(90deg,#e6e6e6,#cfcfcf 60%,#d9d9d9)}
.hero-visual{position:absolute;left:410px;top:40px;width:420px;height:380px;background:radial-gradient(circle at 50% 50%,#8a8a8a,#2a2a2a 70%,transparent 72%);opacity:.9}
.hero-kicker{position:absolute;left:83px;top:150px;font-size:21px;font-weight:500;color:#333}
.hero-title{position:absolute;left:83px;top:180px;font-size:27px;font-weight:700;color:#222}
.hero-rule{position:absolute;left:83px;top:222px;width:44px;height:2px;background:#222}
.hero-cta{position:absolute;left:83px;top:254px;font-size:17px;color:var(--red)}
.promo-line{left:0;top:685px;width:1200px;text-align:center;font-size:13px}
.promo-line a{color:var(--red);text-decoration:underline}

/* categories */
.cat{top:742px;width:282px;height:193px;padding:22px 0 0 30px}
.cat h3{font-size:21px;font-weight:700;text-transform:uppercase;line-height:22px}
.cat span{display:block;font-size:11px;font-weight:700;text-decoration:underline;margin-top:2px}
.cat-bins{left:162px;background:linear-gradient(160deg,#1d4e84,#2a6fc4);color:var(--white)}
.cat-glass{left:458px;background:linear-gradient(160deg,#d8dcdc,#b9bfbf);color:#222}
.cat-tumblers{left:756px;background:linear-gradient(160deg,#e8f7b6,#f3cfd2 70%,#d7e6f5);color:var(--red)}

/* about */
.about-visual{left:162px;top:1020px;width:388px;height:280px;background:linear-gradient(90deg,#fff 0,#2b1f24 20%,#111 50%,#e58a2b 90%,#fff);border-radius:4px}
.about-text{left:585px;top:1055px;width:410px;text-align:center}
.about-text h2{font-size:28px;font-weight:700;line-height:32px}
.about-text p{margin-top:26px;font-size:14px;line-height:27px;color:var(--muted)}
.about-text a{display:inline-block;margin-top:18px;font-size:14px;text-decoration:underline}

/* product rails */
.rail-head{left:0;width:1200px;text-align:center;font-size:22px;font-weight:700;color:var(--red)}
.rail-head::before,.rail-head::after{content:"";display:inline-block;width:80px;height:1px;background:var(--line);vertical-align:middle;margin:0 18px}
.rail-arrow{font-size:20px}
.product{width:205px}
.product .thumb{height:260px;background:var(--card);display:flex;align-items:center;justify-content:center}
.product .thumb div{width:120px;height:100px;border-radius:8px}
.product h4{margin:18px 0 0 6px;font-size:14px;font-weight:400}
.stars{margin:4px 0 0 6px;font-size:14px;color:var(--star);letter-spacing:2px}
.stars i{font-style:normal;color:var(--star-off)}
.product hr{border:0;border-top:1px solid var(--line);margin:8px 0 0}
.price{margin:10px 0 0 6px;font-size:15px}

/* winter savings */
.winter-text{left:162px;top:1965px;width:426px;text-align:center}
.winter-text h2{font-size:28px;font-weight:700}
.winter-text p{margin-top:14px;font-size:14px;line-height:27px;color:var(--muted)}
.btn-red{display:inline-block;margin-top:28px;width:144px;height:36px;line-height:36px;background:var(--red);color:var(--white);font-weight:700;font-size:15px}
.winter-visual{left:585px;top:1915px;width:420px;height:300px;background:linear-gradient(135deg,#fff 10%,#222 30%,#0a0a0a 70%,#fff 90%)}
.partner{top:2295px;width:94px;height:40px;border-radius:3px;background:#9a9a9a}

/* features */
.feature-visual{left:162px;top:2967px;width:427px;height:331px;background:linear-gradient(100deg,#f0ece8,#cfc7c0 50%,#1f7f85 75%,#d8d1c9)}
.features{left:589px;top:2967px;width:449px;height:331px;display:grid;grid-template-columns:1fr 1fr;grid-template-rows:1fr 1fr}
.feature{display:flex;flex-direction:column;align-items:center;justify-content:center;gap:12px;font-size:14px;font-weight:500;text-transform:uppercase;border-color:var(--line);border-style:solid;border-width:0}
.feature:nth-child(1){border-right-width:1px;border-bottom-width:1px}
.feature:nth-child(2){border-bottom-width:1px}
.feature:nth-child(3){border-right-width:1px}

/* footer */
.footer-rule{left:0;top:3343px;width:1200px;height:1px;background:var(--line)}
.social{left:170px;top:3396px;display:flex;gap:22px}
.social span{width:12px;height:12px;border-radius:50%;background:var(--ink)}
.brand-foot{top:3380px}
.payments{left:830px;top:3394px;display:flex;gap:6px}
.payments span{width:34px;height:20px;border-radius:2px;background:#8a8fa0}
.newsletter{left:355px;top:3490px;width:500px;height:42px;background:#f1f1f1;display:flex;align-items:center}
.newsletter span{flex:1;padding-left:24px;font-size:11px;color:#999}
.newsletter b{width:42px;height:42px;background:var(--red);display:flex;align-items:center;justify-content:center}
.footer-nav{top:3590px;left:0;width:1200px;display:flex;justify-content:center;gap:24px;font-size:16px}
.copyright{top:3625px;left:0;width:1200px;text-align:center;font-size:12px;color:var(--muted)}
</style>
</head>
<body>

<header>
  <div class="abs topbar-links">Become a New Customer | Location</div>
  <div class="abs brand brand-top">Quillfern<br>Housewares</div>
  <div class="abs header-icons">
    <svg width="16" height="16" viewBox="0 0 16 16" fill="none" stroke="#1c1c1c" stroke-width="2"><circle cx="6.5" cy="6.5" r="5"/><path d="M10 10l5 5"/></svg>
    <svg width="16" height="16" viewBox="0 0 16 16" fill="none" stroke="#1c1c1c" stroke-width="1.8"><circle cx="8" cy="5" r="3.5"/><path d="M1.5 15c1-4 12-4 13 0"/></svg>
  </div>
  <div class="abs cart-box">
    <svg width="18" height="20" viewBox="0 0 18 20" fill="#fff"><path d="M1 6h16l-1 13H2z"/><path d="M5 6V4a4 4 0 018 0v2" fill="none" stroke="#fff" stroke-width="2"/></svg>
    <span class="cart-count">0</span>
  </div>
  <div class="abs header-rule"></div>
  <nav class="abs main-nav"><a>HOME</a><a>ABOUT US</a><a>OUR PRODUCTS</a><a>CATEGORY</a><a>BLOGS</a><a>CONTACT US</a></nav>
</header>

<section class="abs hero">
  <div class="hero-visual" role="img" aria-label="Two black wall clocks on a whitewashed wooden background"></div>
  <div class="hero-kicker">SHOP MODERN</div>
  <div class="hero-title">HOUSEWARE PRODUCS</div>
  <div class="hero-rule"></div>
  <a class="hero-cta">SHOP NOW</a>
</section>
<p class="abs promo-line">LIMITED-TIME OFERS : MID-SUMMER SEASON SALE ON SELECTED ITEMS - <a>SHOP NOW</a></p>

<a class="abs cat cat-bins" role="img" aria-label="Blue plastic storage bins"><h3>Storage Bins</h3><span>VIEW ALL</span></a>
<a class="abs cat cat-glass" role="img" aria-label="Clear glass jars"><h3>Glass Prducts</h3><span>VIEW ALL</span></a>
<a class="abs cat cat-tumblers" role="img" aria-label="Colourful tumblers and drinking jars with straws"><h3>Tumblers &amp; Jars</h3><span>VIEW ALL</span></a>

<div class="abs about-visual" role="img" aria-label="Room spray bottles in a display box"></div>
<section class="abs about-text">
  <h2>ABOUT QUILLFERN<br>HOUSEWARE</h2>
  <p>Morbi porta libero id ullamcorper nonummy nibh ligula pulvinar metus eget consectetuer augue nisi quis lacus Ut ac mi quis lacus mollis aliquam vvscelerisque mi tortor at ipsum cligula augue bibendum accumsan</p>
  <a>READ MORE</a>
</section>

<span class="abs rail-arrow" style="left:164px;top:1393px">&larr;</span>
<h2 class="abs rail-head" style="top:1392px">NEW ARRIVALS</h2>
<span class="abs rail-arrow" style="left:1012px;top:1393px">&rarr;</span>

<div class="abs product" style="left:162px;top:1457px"><div class="thumb"><div role="img" aria-label="Pack of small flashlights" style="background:linear-gradient(90deg,#333,#2a78c8,#c33)"></div></div><h4>Product Title here</h4><div class="stars">★★★<i>★★</i></div><hr><div class="price">$25.99</div></div>
<div class="abs product" style="left:386px;top:1457px"><div class="thumb"><div role="img" aria-label="Boxed light bulb" style="width:60px;background:linear-gradient(#eee,#b22)"></div></div><h4>Product Title here</h4><div class="stars">★★★<i>★★</i></div><hr><div class="price">$25.99</div></div>
<div class="abs product" style="left:610px;top:1457px"><div class="thumb"><div role="img" aria-label="Coiled extension cord" style="background:linear-gradient(135deg,#c96a3a,#ddd,#555)"></div></div><h4>Product Title here</h4><div class="stars">★★★<i>★★</i></div><hr><div class="price">$25.99</div></div>
<div class="abs product" style="left:834px;top:1457px"><div class="thumb"><div role="img" aria-label="Clear glass bowl" style="border-radius:50%;background:radial-gradient(#fff,#bbb)"></div></div><h4>Product Title here</h4><div class="stars">★★★<i>★★</i></div><hr><div class="price">$25.99</div></div>

<section class="abs winter-text">
  <h2>WINTER SAVINGS</h2>
  <p>Morbi porta libero id ullamcorper nonummy nibh ligula pulvinar metus eget consectetuer augue nisi quis lacus Ut ac mi quis lacus mollis aliquam vvscelerisque mi tortor at ipsum cligula augue bibendum accumsan vestibulum ut</p>
  <a class="btn-red">VIEW ALL</a>
</section>
<div class="abs winter-visual" role="img" aria-label="Black ashtrays in a display box"></div>

<div class="abs partner" style="left:180px"></div>
<div class="abs partner" style="left:335px"></div>
<div class="abs partner" style="left:492px;background:#111"></div>
<div class="abs partner" style="left:638px;background:#bbb"></div>
<div class="abs partner" style="left:786px;background:#777"></div>
<div class="abs partner" style="left:922px"></div>

<span class="abs rail-arrow" style="left:172px;top:2436px">&larr;</span>
<h2 class="abs rail-head" style="top:2435px">BEST SELLERS</h2>
<span class="abs rail-arrow" style="left:1016px;top:2436px">&rarr;</span>

<div class="abs product" style="left:167px;top:2500px"><div class="thumb"><div role="img" aria-label="Room spray display box" style="background:linear-gradient(90deg,#222,#c33,#e8a23a)"></div></div><h4>Product Title here</h4><div class="stars">★★★<i>★★</i></div><hr><div class="price">$25.99</div></div>
<div class="abs product" style="left:391px;top:2500px"><div class="thumb"><div role="img" aria-label="Room spray display box" style="background:linear-gradient(90deg,#222,#e3b21e,#c33)"></div></div><h4>Product Title here</h4><div class="stars">★★★<i>★★</i></div><hr><div class="price">$25.99</div></div>
<div class="abs product" style="left:616px;top:2500px"><div class="thumb"><div role="img" aria-label="White ceramic mug" style="width:80px;background:linear-gradient(90deg,#ddd,#fff,#ccc)"></div></div><h4>Product Title here</h4><div class="stars">★★★<i>★★</i></div><hr><div class="price">$25.99</div></div>
<div class="abs product" style="left:840px;top:2500px"><div class="thumb"><div role="img" aria-label="White serving bowl" style="height:70px;border-radius:0 0 60px 60px;background:linear-gradient(#ccc,#fff)"></div></div><h4>Product Title here</h4><div class="stars">★★★<i>★★</i></div><hr><div class="price">$25.99</div></div>

<div class="abs feature-visual" role="img" aria-label="Styled living room with a teal armchair and patterned wall art"></div>
<section class="abs features">
  <div class="feature">
    <svg width="62" height="44" viewBox="0 0 62 44" fill="none" stroke="#e0141e" stroke-width="2.5"><rect x="2" y="6" width="36" height="26"/><path d="M38 14h12l9 10v8H38"/><circle cx="14" cy="36" r="5" fill="#fff"/><circle cx="48" cy="36" r="5" fill="#fff"/></svg>
    Free Shipping</div>
  <div class="feature">
    <svg width="50" height="50" viewBox="0 0 50 50" fill="none" stroke="#e0141e" stroke-width="2.5"><path d="M25 3l21 10v24L25 47 4 37V13z"/><path d="M4 13l21 10 21-10M25 23v24"/></svg>
    Best Products</div>
  <div class="feature">
    <svg width="48" height="50" viewBox="0 0 48 50" fill="none" stroke="#e0141e" stroke-width="2.5"><path d="M6 28V22a18 18 0 0136 0v6"/><rect x="3" y="26" width="9" height="14" rx="3"/><rect x="36" y="26" width="9" height="14" rx="3"/><path d="M40 40c0 6-8 8-14 8"/></svg>
    24/7 Support</div>
  <div class="feature">
    <svg width="52" height="52" viewBox="0 0 52 52" fill="none" stroke="#e0141e" stroke-width="2.5"><circle cx="26" cy="26" r="23"/><path d="M15 27l8 8 15-17"/></svg>
    Special Offers</div>
</section>

<footer>
  <div class="abs footer-rule"></div>
  <div class="abs social"><span></span><span></span><span></span><span></span><span></span></div>
  <div class="abs brand brand-foot">Quillfern<br>Housewares</div>
  <div class="abs payments"><span></span><span></span><span></span><span></span><span></span></div>
  <div class="abs newsletter"><span>Get daily updates</span><b><svg width="16" height="16" viewBox="0 0 16 16" fill="#fff"><path d="M1 7L15 1 10 15 8 9z"/></svg></b></div>
  <nav class="abs footer-nav"><a>HOME</a><a>ABOUT US</a><a>OUR PRODUCTS</a><a>CATEGORY</a><a>BLOGS</a><a>CONTACT US</a></nav>
  <p class="abs copyright">© 2018 COMPANY NAME ALL RIGHT RESERVED TERM OF USE</p>
</footer>

</body>
</html>
```